Vantor - Transport company looking for a basic but smart design for the sides of our trailers

We have a logo 'Vantor' which i would like to keep.
We have 2 companies Vantor Haulage - Maroon signwriting (general freight ) and Vantor Refrigerated - Blue signwriting (refrigerated freight) that can share the same design.
I'd like to come up with a basic modern design that will incorporate the Vantor logo, the company name and the website and maybe an image at the front od some sort, a 3D swish or a stripe or something.
The Vantor Haulage maroon trailers are too busy and I don't like the icicles on the front of the Vantor Refrigerated blue trailers.

```html
<!DOCTYPE html>
<html lang="en">
<head>
<meta charset="utf-8">
<title>Vantor Haulage – Trailer Side</title>
<link href="https://fonts.googleapis.com/css2?family=Montserrat:wght@800&family=Lexend:wght@600&display=swap" rel="stylesheet">
<style>
  :root {
    --backdrop: #8a8a8a;
    --maroon: #b91f14;
    --charcoal: #34363c;
    --panel: #ffffff;
    --tint: #e4eef0;
    --stripe: #e6a3a0;
    --contact: #ffffff;
  }
  html, body {
    margin: 0;
    width: 1003px;
    height: 1200px;
    overflow: hidden;
    background: var(--backdrop);
  }
  .trailer-side {
    position: absolute;
    left: 31px;
    top: 460px;
    width: 940px;
    height: 281px;
  }
  .trailer-side svg { display: block; width: 100%; height: 100%; }
  .brand-name {
    font-family: "Montserrat", sans-serif;
    font-weight: 800;
    fill: var(--maroon);
  }
  .contact-line {
    font-family: "Lexend", sans-serif;
    font-weight: 600;
    fill: var(--contact);
  }
</style>
</head>
<body>
<section class="trailer-side" aria-label="Vantor Haulage trailer side artwork">
  <svg viewBox="0 0 1645 492" xmlns="http://www.w3.org/2000/svg">
    <defs>
      <linearGradient id="panel-tint" x1="0" y1="0" x2="1" y2="0">
        <stop offset="0" stop-color="var(--panel)"/>
        <stop offset="0.35" stop-color="var(--panel)"/>
        <stop offset="1" stop-color="var(--tint)"/>
      </linearGradient>
      <linearGradient id="stripe-fade" x1="0" y1="0" x2="0" y2="1">
        <stop offset="0" stop-color="var(--stripe)" stop-opacity="1"/>
        <stop offset="1" stop-color="var(--stripe)" stop-opacity="0.2"/>
      </linearGradient>
    </defs>

    <rect class="panel" width="1645" height="492" fill="url(#panel-tint)"/>

    <g class="speed-stripes" stroke="url(#stripe-fade)" stroke-width="1.6">
      <line x1="0" y1="3" x2="1645" y2="3"/>
      <line x1="0" y1="11" x2="1645" y2="11"/>
      <line x1="0" y1="19" x2="1645" y2="19"/>
      <line x1="0" y1="27" x2="1645" y2="27"/>
      <line x1="0" y1="35" x2="1645" y2="35"/>
      <line x1="0" y1="43" x2="1645" y2="43"/>
      <line x1="0" y1="51" x2="1645" y2="51"/>
      <line x1="0" y1="59" x2="1645" y2="59"/>
      <line x1="0" y1="67" x2="1645" y2="67"/>
      <line x1="0" y1="77" x2="1645" y2="77"/>
      <line x1="0" y1="88" x2="1645" y2="88"/>
      <line x1="0" y1="100" x2="1645" y2="100"/>
    </g>

    <path class="swoosh-shadow" fill="var(--charcoal)"
      d="M0 322 C 110 375, 300 398, 470 396 C 800 390, 1250 318, 1645 340 L1645 492 L0 492 Z"/>
    <path class="swoosh-band" fill="var(--maroon)"
      d="M0 350 C 130 385, 300 398, 470 396 C 800 392, 1300 352, 1645 380 L1645 492 L0 492 Z"/>

    <text class="brand-name" x="190" y="295" font-size="132">Vantor</text>
    <text class="brand-name" x="690" y="280" font-size="172" textLength="845" lengthAdjust="spacingAndGlyphs">HAULAGE</text>

    <g class="phone-icon" fill="none" stroke="var(--contact)" stroke-width="6" stroke-linecap="round">
      <path d="M133 430 c -6 14, 8 34, 26 38 l 6 -10 l -10 -8 l -6 5 c -6 -3, -10 -9, -11 -15 l 6 -4 l -5 -12 Z" fill="var(--contact)" stroke-width="2"/>
      <path d="M152 428 a 14 14 0 0 1 14 14"/>
      <path d="M153 416 a 26 26 0 0 1 26 26"/>
    </g>
    <text class="contact-line" x="186" y="462" font-size="58">(08) 5550 4182</text>

    <line class="divider" x1="677" y1="420" x2="677" y2="462" stroke="var(--contact)" stroke-width="5"/>

    <g class="globe-icon" fill="none" stroke="var(--contact)" stroke-width="3.5">
      <circle cx="733" cy="443" r="16"/>
      <ellipse cx="733" cy="443" rx="7" ry="16"/>
      <line x1="717" y1="443" x2="749" y2="443"/>
      <line x1="733" y1="427" x2="733" y2="459"/>
    </g>
    <text class="contact-line" x="768" y="458" font-size="56" textLength="800" lengthAdjust="spacingAndGlyphs">www.vantorhaulage.com.au</text>
  </svg>
</section>
</body>
</html>
```